Business Card Design for Telecommunications and IT Solutions company "OKRA"

BC for telecommunications company name "OKRA" with slogan "Telecom & IT Solutions"

should have the full name as above "OKRA" and the slogan
color reqiured black, red (dark) and white

simple, professional, serious, modern design is required

1 side of business card have a full details, contacts and logo
other side have only the logo, website and full company name "ALOKRA Company for Telecommunications service & Information Technology LLC"

i have attached the logo and current business card sample and note that the logo was changed not the same in the attached business card

Industry/Entity Type

Telecommunications

Contact Information for Business Card

Full name: Omar Nabil Al Hudari
Job title: General Manager
Mobile no: +964xxxxxxxxx
email: omar@okra-tel.example
full name of the company: ALOKRA Company Telecommunications Services & Information Technology LLC.
website: www.okra-tel.example
address: Nakheel Dist. 148/7 JubailaQadim, Basra, Iraq

Requirements
Must have
• two languages in the same side of business card (English, Arabic) for only the name and title

```html
<!DOCTYPE html>
<html lang="en">
<head>
<meta charset="utf-8">
<title>OKRA – Business Cards</title>
<link rel="stylesheet" href="https://fonts.googleapis.com/css2?family=Open+Sans:wght@400;600&family=Noto+Sans+Arabic:wght@400;600&family=Tinos:ital@1&display=swap">
<style>
  :root {
    --backdrop: #3a302b;
    --card: #161616;
    --card-edge: #0b0b0b;
    --white: #ffffff;
    --muted: #d8d8d8;
    --band: #cfcfcf;
    --band-text: #1a1a1a;
    --red: #b5121b;
    --red-line: #7a0d12;
  }
  * { box-sizing: border-box; margin: 0; padding: 0; }
  html, body { width: 1200px; height: 780px; overflow: hidden; }
  body {
    background: var(--backdrop);
    display: flex; align-items: center; justify-content: center; gap: 40px;
    font-family: "Open Sans", sans-serif;
  }
  .card {
    position: relative; width: 540px; height: 310px;
    background: radial-gradient(ellipse at 40% 40%, #222 0%, var(--card) 60%, var(--card-edge) 100%);
    border-radius: 6px; overflow: hidden;
    box-shadow: 0 14px 30px rgba(0,0,0,.5);
    color: var(--white);
  }
  .brand { display: flex; align-items: center; gap: 10px; }
  .brand-name { font-size: 46px; font-weight: 600; letter-spacing: 2px; color: var(--white); line-height: 1; }
  .brand-dot { width: 22px; height: 22px; border-radius: 50%; background: var(--red); }
  .slogan { font-family: "Tinos", serif; font-style: italic; font-size: 17px; color: var(--muted); }
  .band {
    position: absolute; left: 0; right: 0; background: var(--band); color: var(--band-text);
    display: flex; align-items: center;
  }

  /* Front: logo side */
  .card-front .logo-block {
    position: absolute; top: 44px; left: 0; right: 0;
    display: flex; flex-direction: column; align-items: center; gap: 6px;
  }
  .card-front .company {
    position: absolute; top: 158px; left: 0; right: 0; text-align: center;
  }
  .company-name { font-size: 20px; font-weight: 600; }
  .company-full { font-size: 9.5px; color: var(--muted); margin-top: 3px; }
  .card-front .band { top: 222px; height: 36px; justify-content: center; }
  .company-ar { font-family: "Noto Sans Arabic", sans-serif; font-size: 15px; font-weight: 600; direction: rtl; }

  /* Back: contact side */
  .card-back .logo-block {
    position: absolute; top: 78px; left: 40px; width: 240px;
    display: flex; flex-direction: column; align-items: center; gap: 6px;
  }
  .divider { position: absolute; left: 300px; top: 30px; width: 2px; height: 180px; background: var(--red-line); }
  .contact { position: absolute; left: 322px; top: 36px; right: 16px; }
  .person-name { font-size: 19px; font-weight: 600; line-height: 1.15; }
  .person-title { font-size: 12px; color: var(--muted); }
  .ar { font-family: "Noto Sans Arabic", sans-serif; direction: rtl; text-align: left; unicode-bidi: plaintext; }
  .person-name-ar { font-size: 16px; font-weight: 600; margin-top: 6px; }
  .person-title-ar { font-size: 10.5px; color: var(--muted); }
  .contact-list { list-style: none; margin-top: 12px; }
  .contact-list li { display: flex; align-items: center; gap: 8px; font-size: 12.5px; line-height: 20px; }
  .icon { width: 14px; height: 14px; border-radius: 50%; background: var(--red); display: flex; align-items: center; justify-content: center; flex: none; }
  .card-back .band { top: 236px; height: 38px; padding-left: 30px; }
  .address { font-size: 15px; font-weight: 600; letter-spacing: .3px; }
</style>
</head>
<body>

<section class="card card-front" aria-label="Business card, logo side">
  <div class="logo-block">
    <div class="brand"><span class="brand-name">OKRA</span><span class="brand-dot"></span></div>
    <div class="slogan">Telecom &amp; IT Solutions</div>
  </div>
  <div class="company">
    <div class="company-name">ALOKRA Company</div>
    <div class="company-full">Telecommunications Services &amp; Information Technology LLC.</div>
  </div>
  <div class="band">
    <span class="company-ar">شركة العقرة لخدمات الاتصالات و تقنية المعلومات المحدودة</span>
  </div>
</section>

<section class="card card-back" aria-label="Business card, contact side">
  <div class="logo-block">
    <div class="brand"><span class="brand-name">OKRA</span><span class="brand-dot"></span></div>
    <div class="slogan">Telecom &amp; IT Solutions</div>
  </div>
  <div class="divider"></div>
  <div class="contact">
    <div class="person-name">Omar Nabil Al Hudari</div>
    <div class="person-title">General Manager</div>
    <div class="ar person-name-ar">عمر نبيل الحضري</div>
    <div class="ar person-title-ar">المدير المفوض</div>
    <ul class="contact-list">
      <li><span class="icon"><svg width="8" height="8" viewBox="0 0 10 10"><path d="M2 1 L4 1 L4.6 3.2 L3.4 4 Q4.3 5.8 6 6.6 L6.8 5.4 L9 6 L9 8 Q5 9 2.2 6 Q0.6 3.8 2 1Z" fill="#fff"/></svg></span>+964xxxxxxxxx</li>
      <li><span class="icon"><svg width="8" height="8" viewBox="0 0 10 10"><rect x="1" y="2.5" width="8" height="5.5" fill="none" stroke="#fff" stroke-width="1"/><path d="M1 2.5 L5 5.5 L9 2.5" fill="none" stroke="#fff" stroke-width="1"/></svg></span>omar@okra-tel.example</li>
      <li><span class="icon"><svg width="9" height="9" viewBox="0 0 10 10"><circle cx="5" cy="5" r="3.8" fill="none" stroke="#fff" stroke-width="0.9"/><path d="M1.2 5 H8.8 M5 1.2 Q2.8 5 5 8.8 M5 1.2 Q7.2 5 5 8.8" fill="none" stroke="#fff" stroke-width="0.8"/></svg></span>www.okra-tel.example</li>
    </ul>
  </div>
  <div class="band">
    <span class="address">Nakheel Dist. 148/7 JubailaQadim, Basra, Iraq</span>
  </div>
</section>

</body>
</html>
```